Business Card Design for Varnok Facility Services

We are looking for a Business Card Design for the Company "Varnok Facility Services."
Front side:
- Company Logo (small)
- Company Name, address, pohone, website and personal data.
- white background, for text e.g. company colors (blue or green like in the logo)
Please use following data:
Company data:
Varnok Facility Services Tulbrecht
Kirchmattweg 12
6331 Cham
www.varnok-fs.ch
Person data:
Ruben Tulbrecht
Geschäftsführer
+41 76 519 84 60
info@varnok-fs.ch
Back side:
could be colored in blue or green
please use a big logo sing and some smaller icons to say what is all beeing offered in facility services, like cleaning, maintenance cleaning
industrial cleaning, caretaking, gardening, disposal. There is no need for everyone of the icons if there are similar or an icon is standing for more of them.
Cleaning Service
colors to use:
blue: HEX 246BB0
green: HEX 52B33E

```html
<!DOCTYPE html>
<html lang="de">
<head>
<meta charset="utf-8">
<title>Varnok Facility Services – Visitenkarte</title>
<link href="https://fonts.googleapis.com/css2?family=Arimo:wght@400;700&display=swap" rel="stylesheet">
<style>
  :root {
    --blue: #246BB0;
    --green: #52B33E;
    --grey-band: #dcdfe2;
    --paper: #ffffff;
    --backdrop: #d9d9db;
    --divider: #c9ccd0;
    --icon-tint: #e3f3df;
  }
  * { box-sizing: border-box; margin: 0; padding: 0; }
  html, body { width: 1200px; height: 947px; overflow: hidden; }
  body {
    background: var(--backdrop);
    font-family: "Arimo", Arial, sans-serif;
    display: flex;
    align-items: center;
    justify-content: center;
    gap: 40px;
  }
  .card {
    position: relative;
    width: 540px;
    height: 300px;
    background: var(--paper);
    border-radius: 16px;
    overflow: hidden;
  }
  .card-waves { position: absolute; inset: 0; width: 100%; height: 100%; }

  /* Front */
  .front-brand {
    position: absolute;
    left: 36px; top: 92px;
    width: 250px;
    display: flex;
    align-items: center;
    gap: 12px;
  }
  .brand-dot {
    flex: none;
    width: 22px; height: 22px;
    border-radius: 50%;
    background: var(--green);
  }
  .brand-name {
    color: var(--blue);
    font-weight: 700;
    font-size: 26px;
    line-height: 1.1;
  }
  .front-divider {
    position: absolute;
    left: 294px; top: 68px;
    width: 1px; height: 144px;
    background: var(--divider);
  }
  .contact {
    position: absolute;
    left: 318px; top: 66px;
    color: var(--blue);
    font-size: 13px;
  }
  .contact-name { color: var(--green); font-weight: 700; font-size: 17px; }
  .contact-role { margin-top: 2px; }
  .contact-lines { list-style: none; margin-top: 18px; }
  .contact-lines li { display: flex; align-items: center; gap: 8px; line-height: 19px; }
  .contact-lines svg { width: 11px; height: 11px; flex: none; }
  .contact-address { margin-top: 16px; line-height: 17px; font-style: normal; }

  /* Back */
  .back-brand {
    position: absolute;
    left: 0; right: 0; top: 64px;
    display: flex;
    align-items: center;
    justify-content: center;
    gap: 14px;
  }
  .back-brand .brand-dot { width: 28px; height: 28px; }
  .back-brand .brand-name { color: var(--paper); font-size: 32px; }
  .services {
    position: absolute;
    left: 12px; right: 12px; top: 236px;
    display: flex;
    list-style: none;
  }
  .service {
    flex: 1;
    display: flex;
    justify-content: center;
    border-left: 1px solid var(--divider);
  }
  .service:first-child { border-left: none; }
  .service-icon {
    width: 32px; height: 32px;
    border-radius: 6px;
    background: var(--icon-tint);
  }
</style>
</head>
<body>

  <section class="card card-front" aria-label="Vorderseite">
    <svg class="card-waves" viewBox="0 0 540 300" preserveAspectRatio="none" aria-hidden="true">
      <path d="M0,274 C170,246 390,242 540,288 L540,300 L0,300 Z" fill="var(--green)"/>
      <path d="M0,284 C170,256 390,252 540,296 L540,300 L0,300 Z" fill="var(--paper)"/>
      <path d="M150,300 C290,262 440,262 540,294 L540,300 Z" fill="var(--blue)"/>
    </svg>

    <div class="front-brand">
      <span class="brand-dot"></span>
      <span class="brand-name">Varnok Facility Services</span>
    </div>

    <div class="front-divider"></div>

    <div class="contact">
      <p class="contact-name">RUBEN TULBRECHT</p>
      <p class="contact-role">Geschäftsführer</p>
      <ul class="contact-lines">
        <li>
          <svg viewBox="0 0 12 12"><path d="M3 1 L5 3.5 L4 5 C4.6 6.4 5.6 7.4 7 8 L8.5 7 L11 9 L10 11 C5.5 11 1 6.5 1 2 Z" fill="var(--green)"/></svg>
          +41 76 519 84 60
        </li>
        <li>
          <svg viewBox="0 0 12 12"><rect x="0.5" y="2" width="11" height="8" fill="var(--green)"/><path d="M0.5 2 L6 6.5 L11.5 2" fill="none" stroke="var(--paper)" stroke-width="1"/></svg>
          info@varnok-fs.ch
        </li>
        <li>
          <svg viewBox="0 0 12 12" fill="none" stroke="var(--green)" stroke-width="1"><circle cx="6" cy="6" r="5"/><ellipse cx="6" cy="6" rx="2.2" ry="5"/><path d="M1 6 H11"/></svg>
          www.varnok-fs.ch
        </li>
      </ul>
      <address class="contact-address">Kirchmattweg 12<br>6331 Cham</address>
    </div>
  </section>

  <section class="card card-back" aria-label="Rückseite">
    <svg class="card-waves" viewBox="0 0 540 300" preserveAspectRatio="none" aria-hidden="true">
      <path d="M0,176 C120,182 250,206 360,198 C440,192 500,172 540,160 L540,176 C480,196 420,214 340,216 C230,218 120,196 0,194 Z" fill="var(--green)"/>
      <path d="M0,168 C120,172 250,196 360,190 C440,186 500,166 540,152 L540,164 C490,182 430,200 350,204 C240,208 120,186 0,182 Z" fill="var(--grey-band)"/>
      <path d="M0,0 H540 V148 C490,168 430,186 350,190 C240,194 120,168 0,164 Z" fill="var(--blue)"/>
    </svg>

    <div class="back-brand">
      <span class="brand-dot"></span>
      <span class="brand-name">Varnok Facility Services</span>
    </div>

    <ul class="services">
      <li class="service"><span class="service-icon" role="img" aria-label="Icon Fensterreinigung"></span></li>
      <li class="service"><span class="service-icon" role="img" aria-label="Icon Unterhaltsreinigung"></span></li>
      <li class="service"><span class="service-icon" role="img" aria-label="Icon Industriereinigung"></span></li>
      <li class="service"><span class="service-icon" role="img" aria-label="Icon Hauswartung"></span></li>
      <li class="service"><span class="service-icon" role="img" aria-label="Icon Gartenpflege"></span></li>
      <li class="service"><span class="service-icon" role="img" aria-label="Icon Entsorgung"></span></li>
    </ul>
  </section>

</body>
</html>
```